依頼概要
毎年、全社員の名前、顔写真、誕生日、ひと言コメントを掲載した冊子を作成しています。これまでは表紙について、自社でデザインを実施していましたがロゴ等を並列のするのみのデザイン性に乏しいものでした。
この名鑑を社員一人一人が手にしたときに、ワクワクする!すぐに読みたい!テンションがUPする!というようなデザインにしたいと考えています。
スピード重視ですので、あまり凝ったデザインでなくても良いかなと考えています。

なお、名鑑は2法人(社会福祉法人光彩苑と学校法人桐谷学園)で共同で使用いたします。

法人の理念は、
For The Community~地域のために私たちができること~

となります。

法人のイメージカラーは、オレンジと緑です。

素晴らしいご提案を頂戴できるように楽しみにしています。

```html
<!DOCTYPE html>
<html lang="ja">
<head>
<meta charset="utf-8">
<title>スタッフ年鑑2015 表紙</title>
<link rel="stylesheet" href="https://fonts.googleapis.com/css2?family=Oswald:wght@700&family=M+PLUS+1p:wght@500;800&display=swap">
<style>
  :root {
    --green: #7cbf2a;
    --green-deep: #4e9a1c;
    --green-light: #c7e37a;
    --orange: #ee7a1e;
    --ink: #4a4a4a;
    --paper: #ffffff;
  }
  * { margin: 0; padding: 0; box-sizing: border-box; }
  html, body { width: 849px; height: 1200px; overflow: hidden; background: var(--paper); }
  .cover {
    position: relative;
    width: 849px;
    height: 1200px;
    overflow: hidden;
    background: var(--paper);
    font-family: "M PLUS 1p", sans-serif;
  }
  .motto {
    position: absolute;
    left: 0; top: 0;
    width: 849px; height: 480px;
  }
  .motto text {
    font-family: "Oswald", sans-serif;
    font-weight: 700;
  }
  .publishers {
    position: absolute;
    right: 40px; top: 34px;
    text-align: right;
    color: var(--ink);
  }
  .publisher-main {
    display: flex; align-items: center; justify-content: flex-end; gap: 10px;
  }
  .publisher-mark {
    width: 30px; height: 30px; border-radius: 50%;
    background: var(--orange);
  }
  .publisher-name {
    font-size: 34px; font-weight: 800; color: var(--green-deep); letter-spacing: 1px;
  }
  .publisher-sub { font-size: 11px; margin-top: 2px; font-weight: 500; }
  .school { margin-top: 16px; font-size: 14px; font-weight: 500; }
  .school strong { font-size: 22px; font-weight: 800; margin-left: 6px; }
  .title-block {
    position: absolute;
    left: 362px; top: 214px;
  }
  .yearbook-title {
    font-size: 48px; font-weight: 800; color: var(--orange); letter-spacing: 1px; line-height: 1.2;
  }
  .yearbook-subtitle {
    font-size: 30px; font-weight: 800; color: var(--green-deep); margin-top: 2px; line-height: 1.2;
  }
  .facilities {
    position: absolute;
    left: 70px; top: 512px;
    width: 720px;
    list-style: none;
    display: flex; flex-wrap: wrap; gap: 30px 40px; align-items: center;
  }
  .facility {
    font-size: 18px; font-weight: 800; color: var(--green-deep); line-height: 1.2;
  }
  .facility.alt { color: var(--orange); }
  .facility.boxed {
    background: var(--green-deep); color: var(--paper);
    padding: 6px 18px; font-size: 22px;
  }
  .celebration {
    position: absolute;
    left: 0; top: 660px;
    width: 849px; height: 540px;
    background: linear-gradient(to bottom, rgba(255,255,255,0) 0%, rgba(199,227,122,0.6) 20%, var(--green) 55%, var(--green-deep) 100%);
  }
</style>
</head>
<body>
<main class="cover">
  <svg class="motto" viewBox="0 0 849 480" aria-label="FOR THE COMMUNITY">
    <defs>
      <linearGradient id="mottoFill" x1="0" y1="0" x2="1" y2="1">
        <stop offset="0" stop-color="#b6d94a"/>
        <stop offset="0.5" stop-color="#7cbf2a"/>
        <stop offset="1" stop-color="#a9d13c"/>
      </linearGradient>
    </defs>
    <text x="26" y="168" font-size="176" fill="url(#mottoFill)" textLength="300" lengthAdjust="spacingAndGlyphs">FOR</text>
    <text x="26" y="318" font-size="176" fill="url(#mottoFill)" textLength="300" lengthAdjust="spacingAndGlyphs">THE</text>
    <text x="26" y="468" font-size="176" fill="url(#mottoFill)" textLength="796" lengthAdjust="spacingAndGlyphs">COMMUNITY</text>
  </svg>

  <header class="publishers">
    <div class="publisher-main">
      <span class="publisher-mark"></span>
      <span class="publisher-name">Kosaien</span>
    </div>
    <p class="publisher-sub">社会福祉法人光彩苑</p>
    <p class="school">学校法人<strong>桐谷学園</strong></p>
  </header>

  <section class="title-block">
    <h1 class="yearbook-title">スタッフ年鑑2015</h1>
    <p class="yearbook-subtitle">地域のために私たちができること</p>
  </section>

  <ul class="facilities">
    <li class="facility">ひだまり保育園</li>
    <li class="facility alt">そよかぜ</li>
    <li class="facility">こもれびの里</li>
    <li class="facility">はなみち</li>
    <li class="facility boxed">hinata</li>
    <li class="facility">みどりの丘保育園</li>
    <li class="facility alt">さくら</li>
    <li class="facility">和心庵</li>
  </ul>

  <div class="celebration" role="img" aria-label="両手を挙げて喜ぶ人々の緑のシルエットと、はじけるカラフルな絵の具のしずく"></div>
</main>
</body>
</html>
```